Business Cards
Stationary for Stainless Steel Abrasives distributor
Bright & Fun-filled
KV Grinding Inc. or Tamsel Bay Grinding Inc.
Avenida Corlinde Via 42 GT 9,
Villa Brezana,
Carolina, PR 00741
info@kelvoquartz.example
www.kelvoquartz.example
I would like to have a black business card with the same colors of my logos
Feel free to contact us for any questions or www.kelvoquartz.example
1. For the envelopes we want to use our postal address instead our physical address:
PO BOX 58314, MERUDA STATION, SAN JUAN PR 00637
2. Business Card use Postal Address plus Physical Address: use both
3. For the business paper we want the postal address that we mentioned in the #1
Cordially
This is the Logo you will be using for the stationary.
Another file you can use.

```html
<!DOCTYPE html>
<html lang="en">
<head>
<meta charset="utf-8">
<title>KV Grinding Inc. – Stationery Set</title>
<link rel="stylesheet" href="https://fonts.googleapis.com/css2?family=Open+Sans:wght@400;700&display=swap">
<style>
  :root {
    --stage: #2e2f31;
    --stage-dark: #222325;
    --ink: #0c0d0f;
    --paper: #ffffff;
    --paper-shade: #eceff1;
    --brand-blue: #1f9ad6;
    --brand-cyan: #36c4f0;
    --brand-deep: #0c5f8f;
    --text-light: #dfe6ea;
    --text-muted: #8a949a;
    --watermark: #e6e9eb;
  }
  * { box-sizing: border-box; margin: 0; padding: 0; }
  html, body { width: 1200px; height: 310px; overflow: hidden; }
  body {
    background: radial-gradient(ellipse at 50% 40%, var(--stage) 0%, var(--stage-dark) 100%);
    font-family: "Open Sans", Arial, sans-serif;
    position: relative;
  }
  .piece { position: absolute; overflow: hidden; box-shadow: 0 2px 6px rgba(0,0,0,.5); }
  .brand { display: flex; align-items: center; gap: 4px; font-weight: 700; color: var(--paper); white-space: nowrap; }
  .brand-square { display: inline-block; background: var(--brand-blue); }
  .brand--dark { color: var(--ink); }
  .wave { position: absolute; left: 0; width: 100%; }
  .watermark {
    position: absolute; left: 0; right: 0; text-align: center;
    font-weight: 700; color: var(--watermark); white-space: nowrap;
  }
  .tiny { font-size: 3.4px; line-height: 1.45; color: var(--text-muted); }

  /* Business card front */
  .card-front { left: 8px; top: 12px; width: 180px; height: 104px; background: var(--ink); }
  .card-front .brand { position: absolute; left: 10px; top: 10px; font-size: 11px; gap: 6px; }
  .card-front .brand-square { width: 14px; height: 14px; }
  .card-front .company { position: absolute; left: 30px; top: 27px; font-size: 8px; font-weight: 700; color: var(--brand-cyan); }
  .card-front .role {
    position: absolute; left: 10px; top: 56px; font-size: 4.5px; color: var(--text-light);
    border: 1px solid var(--text-muted); padding: 2px 5px;
  }

  /* Business card back */
  .card-back { left: 8px; top: 128px; width: 180px; height: 96px; background: var(--ink); }
  .card-back .contact { position: absolute; right: 10px; top: 14px; text-align: right; color: var(--text-light); }

  .card-white { left: 12px; top: 234px; width: 96px; height: 62px; background: var(--paper); }
  .card-white .brand { position: absolute; left: 8px; top: 10px; font-size: 7px; }
  .card-white .brand-square { width: 8px; height: 8px; }
  .card-white .tiny { position: absolute; left: 8px; bottom: 6px; }

  .card-blue { left: 118px; top: 234px; width: 98px; height: 62px;
    background: linear-gradient(135deg, var(--brand-cyan), var(--brand-deep)); }
  .card-blue .brand { position: absolute; left: 12px; top: 24px; font-size: 8px; }
  .card-blue .brand-square { width: 9px; height: 9px; background: var(--paper); }

  /* Letterheads */
  .letterhead { top: 12px; width: 150px; height: 288px; background: var(--paper); }
  .letterhead--a { left: 200px; }
  .letterhead--b { left: 358px; }
  .letterhead .header { position: absolute; left: 0; top: 0; width: 100%; height: 30px; background: var(--ink); }
  .letterhead .brand { position: absolute; left: 8px; top: 9px; font-size: 7px; }
  .letterhead .brand-square { width: 9px; height: 9px; }
  .letterhead .contact { position: absolute; right: 8px; top: 8px; text-align: right; color: var(--text-light); font-size: 3px; }
  .letterhead .watermark { top: 125px; font-size: 16px; }
  .letterhead .footer { position: absolute; left: 0; right: 0; bottom: 6px; text-align: center; font-size: 3px; }

  /* Envelopes */
  .envelope { left: 516px; width: 206px; height: 104px; background: var(--paper); }
  .envelope--top { top: 12px; }
  .envelope--bottom { top: 184px; }
  .envelope .header { position: absolute; left: 0; top: 0; width: 100%; height: 26px; background: var(--ink); }
  .envelope .brand { position: absolute; left: 8px; top: 7px; font-size: 7px; }
  .envelope .brand-square { width: 9px; height: 9px; }
  .envelope .return { position: absolute; left: 8px; top: 30px; font-size: 3.4px; }

  /* Envelope stack */
  .env-stack { left: 740px; top: 12px; width: 452px; height: 288px; overflow: visible; box-shadow: none; }
  .env-back { position: absolute; width: 440px; height: 118px; box-shadow: 0 2px 6px rgba(0,0,0,.5); }
  .env-back--silver { left: 0; top: 0; background: linear-gradient(180deg, #f4f5f6, #b9bfc3); }
  .env-back--blue { left: 8px; top: 74px; background: linear-gradient(180deg, var(--brand-cyan), var(--brand-deep)); }
  .env-back svg { position: absolute; inset: 0; }
  .env-front { position: absolute; left: 12px; top: 158px; width: 440px; height: 128px;
    background: linear-gradient(180deg, var(--paper), var(--paper-shade)); box-shadow: 0 2px 6px rgba(0,0,0,.5); }
  .env-front svg { position: absolute; inset: 0; }
  .env-front .brand { position: absolute; left: 190px; top: 50px; font-size: 9px; }
  .env-front .brand-square { width: 11px; height: 11px; }
</style>
</head>
<body>

  <section class="piece card-front" aria-label="Business card front">
    <div class="brand"><span class="brand-square"></span>KV Grinding Inc.</div>
    <div class="company">Tamsel Bay Grinding Inc.</div>
    <div class="role">Sales Representative</div>
    <svg class="wave" style="bottom:0;height:26px" viewBox="0 0 180 26" preserveAspectRatio="none">
      <path d="M0 14 C50 2 110 26 180 8 L180 26 L0 26 Z" fill="var(--brand-blue)"/>
    </svg>
  </section>

  <section class="piece card-back" aria-label="Business card back">
    <div class="contact tiny">
      Avenida Corlinde Via 42 GT 9, Villa Brezana<br>
      Carolina, PR 00741<br>
      PO BOX 58314, MERUDA STATION<br>
      SAN JUAN PR 00637<br>
      info@kelvoquartz.example<br>
      www.kelvoquartz.example
    </div>
    <svg class="wave" style="bottom:0;height:34px" viewBox="0 0 180 34" preserveAspectRatio="none">
      <path d="M0 10 C60 30 120 0 180 16 L180 34 L0 34 Z" fill="var(--brand-blue)"/>
      <path d="M0 22 C60 34 120 14 180 26 L180 34 L0 34 Z" fill="var(--brand-deep)"/>
    </svg>
  </section>

  <section class="piece card-white" aria-label="Business card white">
    <div class="brand brand--dark"><span class="brand-square"></span>KV Grinding Inc.</div>
    <div class="tiny">www.kelvoquartz.example</div>
  </section>

  <section class="piece card-blue" aria-label="Business card blue">
    <div class="brand"><span class="brand-square"></span>KV Grinding Inc.</div>
  </section>

  <section class="piece letterhead letterhead--a" aria-label="Letterhead">
    <div class="header"></div>
    <svg class="wave" style="top:22px;height:16px" viewBox="0 0 150 16" preserveAspectRatio="none">
      <path d="M0 8 C40 0 100 16 150 4 L150 10 C100 16 40 6 0 14 Z" fill="var(--brand-blue)"/>
    </svg>
    <div class="brand"><span class="brand-square"></span>KV Grinding Inc.</div>
    <div class="contact">info@kelvoquartz.example<br>www.kelvoquartz.example</div>
    <div class="watermark">KV Grinding Inc.</div>
    <div class="footer tiny">PO BOX 58314, MERUDA STATION, SAN JUAN PR 00637</div>
  </section>

  <section class="piece letterhead letterhead--b" aria-label="Letterhead continuation">
    <div class="header"></div>
    <svg class="wave" style="top:22px;height:16px" viewBox="0 0 150 16" preserveAspectRatio="none">
      <path d="M0 8 C40 0 100 16 150 4 L150 10 C100 16 40 6 0 14 Z" fill="var(--brand-blue)"/>
    </svg>
    <div class="brand"><span class="brand-square"></span>KV Grinding Inc.</div>
    <div class="contact">info@kelvoquartz.example<br>www.kelvoquartz.example</div>
    <div class="watermark">KV Grinding Inc.</div>
    <div class="footer tiny">PO BOX 58314, MERUDA STATION, SAN JUAN PR 00637</div>
  </section>

  <section class="piece envelope envelope--top" aria-label="Envelope front">
    <div class="header"></div>
    <svg class="wave" style="top:18px;height:14px" viewBox="0 0 206 14" preserveAspectRatio="none">
      <path d="M0 8 C60 0 140 14 206 4 L206 9 C140 14 60 6 0 13 Z" fill="var(--brand-blue)"/>
    </svg>
    <div class="brand"><span class="brand-square"></span>KV Grinding Inc.</div>
    <div class="return tiny">PO BOX 58314, MERUDA STATION<br>SAN JUAN PR 00637</div>
  </section>

  <section class="piece envelope envelope--bottom" aria-label="Envelope front alternate">
    <div class="header"></div>
    <svg class="wave" style="top:18px;height:14px" viewBox="0 0 206 14" preserveAspectRatio="none">
      <path d="M0 8 C60 0 140 14 206 4 L206 9 C140 14 60 6 0 13 Z" fill="var(--brand-blue)"/>
    </svg>
    <div class="brand"><span class="brand-square"></span>KV Grinding Inc.</div>
    <div class="return tiny">PO BOX 58314, MERUDA STATION<br>SAN JUAN PR 00637</div>
  </section>

  <section class="piece env-stack" aria-label="Envelope set">
    <div class="env-back env-back--silver">
      <svg viewBox="0 0 440 118" preserveAspectRatio="none">
        <path d="M0 0 L220 70 L440 0" fill="none" stroke="#9aa1a6" stroke-width="1"/>
      </svg>
    </div>
    <div class="env-back env-back--blue">
      <svg viewBox="0 0 440 118" preserveAspectRatio="none">
        <path d="M0 0 L220 70 L440 0" fill="none" stroke="var(--brand-deep)" stroke-width="1"/>
      </svg>
    </div>
    <div class="env-front">
      <svg viewBox="0 0 440 128" preserveAspectRatio="none">
        <path d="M0 0 L220 80 L440 0 Z" fill="#f7f8f9" stroke="#c9ced2" stroke-width="1"/>
        <path d="M0 128 L200 70 M440 128 L240 70" stroke="#d6dadd" stroke-width="1"/>
      </svg>
      <div class="brand brand--dark"><span class="brand-square"></span>KV Grinding Inc.</div>
    </div>
  </section>

</body>
</html>
```